Create a 3-4 page concept for an electrical contracting company

We are a company that requires a new look for our website. We are familiar with Sitecraft to be able to update using any theme or builder supplied.

While typical ideas of construction may get the yellow and blue colour pallette, hard hats, hammers, or lightning bolts entering the arena, we are completely against this image.

We intend for the website to have instant appeal and intuitive navigation. The home page should have a creative use of angles or brand identification with the banner or menubar if needed.

After combing hundreds of sitecraft templates, the most attractive seem to be aimed at beauty services. Unfortunately we do not have a lot of picture perfect material to showcase, but it can be blended in other ways. - the brand should be recognizable and captivating.

Target Market(s)

High-end contracting firms focused on quality and service for long term projects (Custom Homes)

Industry/Entity Type

Contracting

Font styles to use
Sans Serif
Other font styles liked:
• Gotham usually. Adjusted kerning and rounded edges seem to be more friendly

Requirements
Must have
• Creative use of the logo shape and colour scheme, especially at the home.

Use of a CMS to be modifiable from a browser (Sitecraft,etc) - A builder such as tandem, kora, or framewell accepted!

Elements or sections that could be adaptable for use. About us, members, contact, services... etc. Content would be written after
Nice to have
• Some clean inspiration that we appreciate:

www.harbelmedia.ca
www.pinwoodbuildworks.com
Should not have
• Generic welcome banner...

```html
<!DOCTYPE html>
<html lang="en">
<head>
<meta charset="utf-8">
<title>Keystone Electric</title>
<link href="https://fonts.googleapis.com/css2?family=Montserrat:ital,wght@0,400;0,500;0,600;0,700;1,400&display=swap" rel="stylesheet">
<style>
:root{
  --bg:#2a2a2b;
  --bg-deep:#1f1f20;
  --card:#1e1e1f;
  --footer:#232324;
  --footer-bar:#1a1a1b;
  --blue:#2b7bbb;
  --white:#ffffff;
  --text:#a9a9a9;
  --muted:#7d7d7d;
  --line:rgba(255,255,255,0.07);
  --field:#2e2e30;
}
*{margin:0;padding:0;box-sizing:border-box}
html,body{width:1200px;height:3499px;overflow:hidden;background:var(--bg)}
body{position:relative;font-family:'Montserrat',sans-serif;color:var(--text)}
.abs{position:absolute}
.grid-line{position:absolute;top:578px;width:1px;height:2544px;background:var(--line)}

/* hero */
.hero{position:absolute;left:0;top:0;width:1200px;height:578px;
  background:linear-gradient(180deg,#1d1f33 0%,#2c2a3a 40%,#3a3026 70%,#25263a 100%)}
.brand{position:absolute;display:flex;align-items:center;gap:10px;color:var(--white);font-weight:600;letter-spacing:1px}
.brand-square{width:38px;height:38px;background:var(--white)}
.brand-name{font-size:19px;line-height:1.05;text-transform:uppercase}
.nav{position:absolute;left:533px;top:47px;display:flex;gap:0;font-size:11px;font-weight:600;letter-spacing:.6px;color:var(--white)}
.nav a{color:inherit;text-decoration:none;margin-right:31px}
.nav a.active{color:var(--blue)}
.social{position:absolute;left:1144px;top:61px;width:56px;height:224px;background:rgba(20,20,25,.55)}
.social span{position:absolute;left:23px;width:10px;height:10px;border-radius:50%;background:#cfcfcf}
.hero-kicker{left:92px;top:222px;font-size:22px;color:var(--white);letter-spacing:1.5px}
.hero-title{left:92px;top:254px;font-size:39px;font-weight:700;color:var(--white);letter-spacing:2.5px}
.hero-text{left:95px;top:318px;width:580px;font-size:15px;line-height:26px;color:var(--white)}
.btn{position:absolute;border:1px solid var(--blue);color:var(--blue);font-size:11px;font-weight:600;letter-spacing:1px;display:flex;align-items:center;justify-content:center;text-transform:uppercase}

.section-title{position:absolute;left:0;width:1200px;text-align:center;font-size:27px;font-weight:600;color:var(--white);letter-spacing:3px}
.section-title em{font-style:normal;color:var(--blue)}

.sub-title{left:122px;top:802px;font-size:21px;font-weight:600;color:var(--white);letter-spacing:2px}
.body-copy{font-size:13px;line-height:21px;color:var(--text)}
.sign-line{left:125px;top:1057px;width:130px;height:1px;background:#444}
.sign{left:127px;top:1073px;font-size:13px;line-height:19px;font-style:italic}
.sign b{font-weight:400;color:var(--white)}

.photo{position:absolute}
.service{position:absolute;top:1397px;width:299px;height:330px}
.service-label{position:absolute;left:34px;bottom:42px;font-size:16px;font-weight:700;color:var(--white);letter-spacing:1.6px;line-height:19px;text-transform:uppercase}

.t-card{position:absolute;top:1962px;height:327px;background:var(--card)}
.avatar{position:absolute;left:42px;top:47px;width:53px;height:53px;background:linear-gradient(135deg,#9fb3c6,#56677a)}
.t-text{position:absolute;left:42px;top:146px;width:270px;font-size:13px;line-height:21px}
.t-name{position:absolute;left:39px;top:261px;font-size:13px;font-style:italic}

.band{position:absolute;left:4px;top:2362px;width:1196px;height:318px;
  background:linear-gradient(90deg,#26262a 0%,#34302c 45%,#2a2827 100%)}

.client{position:absolute;width:170px;display:flex;align-items:center;gap:10px;color:#5c5c5e;font-size:17px;font-weight:600;letter-spacing:2px;text-transform:uppercase}
.client i{display:block;width:22px;height:22px;border-radius:50%;background:#5c5c5e}

.footer{position:absolute;left:0;top:3122px;width:1200px;height:331px;background:var(--footer)}
.footer-bar{position:absolute;left:0;top:3453px;width:1200px;height:46px;background:var(--footer-bar);text-align:center;font-size:9px;line-height:46px;color:#6b6b6b;letter-spacing:.5px}
.contact-line{position:absolute;left:160px;font-size:15px;color:var(--white);letter-spacing:.8px}
.f-link{position:absolute;left:440px;font-size:15px;color:var(--muted);letter-spacing:.8px}
.field{position:absolute;background:var(--field);font-size:10px;color:#8a8a8a;letter-spacing:1px;padding:11px 0 0 16px;text-transform:uppercase}
.send{position:absolute;left:621px;top:3368px;width:105px;height:31px;background:var(--blue);color:var(--white);font-size:12px;font-weight:700;letter-spacing:1.5px;display:flex;align-items:center;justify-content:center}
</style>
</head>
<body>

<div class="grid-line" style="left:102px"></div>
<div class="grid-line" style="left:435px"></div>
<div class="grid-line" style="left:769px"></div>
<div class="grid-line" style="left:1101px"></div>

<header class="hero" role="img" aria-label="Night view of a luxury home with lit windows and a pool in front">
</header>
<div class="brand" style="left:37px;top:38px"><span class="brand-square"></span><span class="brand-name">Keystone<br>Electric</span></div>
<nav class="nav">
  <a class="active">WELCOME</a><a>ABOUT US</a><a>SERVICES</a><a>OURWORKS</a><a>CAREERS</a><a>CONTACT</a>
</nav>
<div class="social">
  <div class="abs" style="left:27px;top:10px;width:1px;height:26px;background:#fff"></div>
  <span style="top:66px"></span><span style="top:111px"></span><span style="top:156px"></span><span style="top:200px"></span>
</div>
<p class="abs hero-kicker">WELCOME TO</p>
<h1 class="abs hero-title">KEYSTONE ELECTRIC</h1>
<p class="abs hero-text">We are a fresh look on the industry, marrying tradition with innovation, and growing with advancements of our field's technology</p>
<div class="btn" style="left:95px;top:406px;width:165px;height:48px">Read More</div>

<h2 class="section-title" style="top:666px">ABOUT <em>KEYSTONE</em></h2>
<h3 class="abs sub-title">WHO WE ARE</h3>
<p class="abs body-copy" style="left:122px;top:852px;width:285px">We are a North Shore electrical contracting company. We are a fresh look on the industry; marrying tradition with innovation, and growing with advancements of our field's technology . Our dedications are in the needs of the clients, and our aim is to surpass them.</p>
<div class="abs sign-line"></div>
<p class="abs sign"><b>Ryan and Colin</b><br>Keystone Electric Inc.</p>
<p class="abs body-copy" style="left:463px;top:852px;width:288px">Established in North Vancouver, Keystone Electric has a history of work in the finest custom projects, to the complexities of any scale of renovation. Our vision is to continue tradition of outstanding workmanship with uncompromising quality and personalized approach, to create a bright and enjoyable experience for our clients.</p>
<div class="photo" style="left:769px;top:805px;width:332px;height:328px;background:linear-gradient(120deg,#e6e4df 0%,#bfb9b0 50%,#8d877f 100%)" role="img" aria-label="Pendant lamps with caged filament bulbs in front of a bright window"></div>

<h2 class="section-title" style="top:1306px">OUR <em>SERVICES</em></h2>
<div class="service" style="left:4px;background:linear-gradient(180deg,#2c2a2a,#4a3a26 55%,#141414)" role="img" aria-label="Modern residential building lit at night">
  <p class="service-label">New Residential<br>Construction</p></div>
<div class="service" style="left:303px;background:linear-gradient(160deg,#8d9aa8,#3b4b66 50%,#6b3526)" role="img" aria-label="Commercial interior with a blue staircase">
  <p class="service-label">Commercial / Tenant<br>Improvements</p></div>
<div class="service" style="left:602px;background:linear-gradient(160deg,#3a4d66,#2e3336 50%,#252525)" role="img" aria-label="Underground utility tunnel with conduit runs">
  <p class="service-label">Overhead / Under-<br>ground Electrical &amp;<br>Telecommunications<br>Services</p></div>
<div class="service" style="left:901px;background:linear-gradient(90deg,#6b6f73,#514b44 50%,#8a7f72)" role="img" aria-label="Wall mounted home automation touch panel">
  <p class="service-label" style="bottom:55px">Lighting Control /<br>Home Automation In-<br>stallations and Ret-<br>rofits</p></div>

<svg class="abs" style="left:535px;top:1759px" width="20" height="18" viewBox="0 0 20 18" aria-hidden="true"><path d="M19 9H2M9 2 2 9l7 7" stroke="#fff" stroke-width="1.6" fill="none"/></svg>
<svg class="abs" style="left:645px;top:1759px" width="20" height="18" viewBox="0 0 20 18" aria-hidden="true"><path d="M1 9h17M11 2l7 7-7 7" stroke="#fff" stroke-width="1.6" fill="none"/></svg>

<h2 class="section-title" style="top:1861px">TESTIMONIALS</h2>
<div class="t-card" style="left:113px;width:312px"><div class="avatar" role="img" aria-label="Client portrait"></div><p class="t-text">Originally, creative and with an innate understanding of their customer's need. The team at Linwell are always a pleasure to work with.</p><p class="t-name">Marco Bellini</p></div>
<div class="t-card" style="left:443px;width:311px"><div class="avatar" role="img" aria-label="Client portrait"></div><p class="t-text">Originally, creative and with an innate understanding of their customer's need. The team at Linwell are always a pleasure to work with.</p><p class="t-name">Marco Bellini</p></div>
<div class="t-card" style="left:780px;width:313px"><div class="avatar" role="img" aria-label="Client portrait"></div><p class="t-text">Originally, creative and with an innate understanding of their customer's need. The team at Linwell are always a pleasure to work with.</p><p class="t-name">Marco Bellini</p></div>

<div class="band" role="img" aria-label="Dim modern kitchen and dining table"></div>
<h2 class="section-title" style="top:2457px">GET IN TOUCH WITH KEYSTONE</h2>
<div class="btn" style="left:503px;top:2536px;width:166px;height:47px">Contact Now</div>

<h2 class="section-title" style="top:2740px">OUR <em>CLIENTS</em></h2>
<div class="client" style="left:110px;top:2856px"><i></i>Harlow Bank</div>
<div class="client" style="left:322px;top:2856px"><i></i>vantera</div>
<div class="client" style="left:528px;top:2856px"><i></i>Harlow Bank</div>
<div class="client" style="left:738px;top:2856px"><i></i>vantera</div>
<div class="client" style="left:944px;top:2856px"><i></i>Harlow Bank</div>
<div class="client" style="left:110px;top:2959px"><i></i>Harlow Bank</div>
<div class="client" style="left:322px;top:2959px"><i></i>vantera</div>
<div class="client" style="left:528px;top:2959px"><i></i>Harlow Bank</div>
<div class="client" style="left:738px;top:2959px"><i></i>vantera</div>
<div class="client" style="left:944px;top:2959px"><i></i>Harlow Bank</div>

<footer class="footer"></footer>
<div class="brand" style="left:105px;top:3170px"><span class="brand-square"></span><span class="brand-name">Keystone<br>Electric</span></div>
<p class="contact-line" style="top:3240px">(604) 555-0143</p>
<p class="contact-line" style="top:3272px">(604) 555-0178</p>
<p class="contact-line" style="top:3303px;color:var(--blue)">office@keystoneelectric.ca</p>
<p class="f-link" style="top:3178px">Home</p>
<p class="f-link" style="top:3210px">About Us</p>
<p class="f-link" style="top:3241px">Services</p>
<p class="f-link" style="top:3273px">Portfolio</p>
<p class="f-link" style="top:3305px">Careers</p>
<p class="f-link" style="top:3336px">Contact</p>
<div class="field" style="left:622px;top:3177px;width:185px;height:32px">Name</div>
<div class="field" style="left:828px;top:3177px;width:184px;height:32px">Email</div>
<div class="field" style="left:622px;top:3228px;width:185px;height:32px">Phone Number</div>
<div class="field" style="left:828px;top:3228px;width:184px;height:32px">Company</div>
<div class="field" style="left:622px;top:3280px;width:390px;height:70px">Message</div>
<div class="send">SEND</div>
<div class="footer-bar">© Copyright - Keystone Electric | North Vancouver, B.C.</div>

</body>
</html>
```